Design for company homepage promoting to the pharmaceutical industry

Our company produces medical education materials and services for the pharmaceutical industry. Our existing website (www.quorvane.net.au) provides more information.
 
We need a homepage design for our new company website we are creating. Our site will not have a great amount of content, we want it to be fast, user friendly and easily adaptable to viewing on any platform, and through any browser. We don't want it over-designed - i.e. no highly animated banner flags, backgrounds, obscure webfonts, too many graphics etc. Attached are files indicating our existing company logo and design. We want the logo and rings to be retained. We've also attached draft copy for the website.
The final website may be designed in Wordpress (still to be confirmed)
 
This is a design to replace the current site (www.quorvane.net.au). Content will also be revised.
Things we don't like about our current design - doesn't use our current branding, is not very exciting, old fashioned 'standard' format, too much content, just doesn't look that good, boring.
 
Examples of sites we like:
www.bralimo.com.au
http://factsheets.tenvoramed.com.au/index.html
 
Features we like from these sites - fast, responsive, short and to the point, cross-platform compatible including smartphones, and looks good
 
Main reasons people will visit our site: to find out whether we can provide services they might be looking for, to make a decision on whether they are interested in what we offer so they can get in touch with us, and to get our contact details.
Main thing we want to achieve from website visits is that it looks good enough and provides enough summary information on us so that they want to get in touch with us, to offer us work or to ask us to come in and meet them to provide more info on what we do.
Two most important calls to action from our website
· make the decision that we can do what you are looking for
· get in touch with us.
Updates

Thanks everyone for your submissions. At this stage with the Christmas break upon us, we are yet to finalise our decision, and will make a decision early in the new year. I hope everyone has a good holiday break.
Kind regards
Giles

Target Market(s)

Pharmaceutical industry professionals, marketers and medical professionals.

Industry/Entity Type

Pharmaceutical

Requirements
Must have
• Company logo and rings must be incorporated, company colour - blue - must be in there.
Should not have
• Complex animation or graphics that will slow the upload or limit cross-platform compatability/viewing on smartphones etc.

```html
<!DOCTYPE html>
<html lang="en">
<head>
<meta charset="utf-8">
<title>Quorvane Healthcare Education</title>
<link href="https://fonts.googleapis.com/css2?family=Roboto:ital,wght@0,300;0,400;0,500;1,400&family=Roboto+Condensed:wght@300;400&display=swap" rel="stylesheet">
<style>
:root{
  --brand:#1d4f86;
  --hero-a:#0f3c70;
  --hero-b:#1b5a99;
  --text:#555;
  --muted:#777;
  --band:#ececec;
  --rule:#dcdcdc;
  --btn-a:#7a7f87;
  --btn-b:#50555d;
  --nav-a:#8b9097;
  --nav-b:#60656c;
  --footer:#3d3d3d;
  --white:#fff;
}
*{margin:0;padding:0;box-sizing:border-box}
html,body{width:926px;height:1200px;overflow:hidden;background:var(--white)}
body{font-family:"Roboto",Arial,sans-serif;color:var(--text);position:relative}
.abs{position:absolute}

/* header */
.logo{left:140px;top:8px;font-weight:400;font-size:30px;line-height:34px;color:var(--brand);letter-spacing:.5px;display:flex;align-items:center;gap:6px}
.logo-dot{width:8px;height:8px;border-radius:50%;background:var(--brand)}
.logo-sub{left:156px;top:45px;font-size:5px;line-height:6px;letter-spacing:1px;color:var(--brand)}
.social{left:582px;top:26px;display:flex;gap:3px}
.social span{width:16px;height:16px;border-radius:50%;background:#d3d3d3}
.btn{background:linear-gradient(var(--btn-a),var(--btn-b));color:var(--white);border:1px solid #44484e;border-radius:3px;display:flex;align-items:center;justify-content:center}
.login{left:709px;top:22px;width:85px;height:27px;font-size:11px}

/* nav */
.nav{left:0;top:68px;width:926px;height:33px;background:linear-gradient(var(--nav-a),var(--nav-b))}
.nav a{position:absolute;top:0;height:33px;line-height:33px;color:var(--white);font-size:9.5px;text-decoration:none}
.nav .active{left:132px;width:101px;text-align:center;background:#55595f}

/* hero */
.hero{left:0;top:101px;width:926px;height:352px;background:linear-gradient(100deg,var(--hero-a),var(--hero-b) 40%,var(--hero-a))}
.hero-art{left:460px;top:101px;width:380px;height:352px;background:radial-gradient(ellipse at 60% 45%,#8fc4f0 0%,#3c7fc2 35%,rgba(15,60,112,0) 70%)}
.hero-title{left:139px;top:178px;font-family:"Roboto Condensed",sans-serif;font-weight:400;font-size:50px;color:var(--white)}
.hero-sub{left:141px;top:240px;font-family:"Roboto Condensed",sans-serif;font-weight:300;font-size:29px;color:var(--white)}
.hero-lead{left:143px;top:285px;font-size:10px;line-height:18.5px;color:var(--white);font-family:"Roboto Condensed",sans-serif;font-weight:300}
.hero-small{left:143px;top:329px;width:300px;font-size:6.5px;line-height:16px;color:var(--white)}
.arrow{width:40px;height:40px}

/* band */
.band{left:0;top:453px;width:926px;height:78px;background:var(--band)}
.band-title{left:133px;top:468px;font-size:12px;font-weight:400;color:var(--brand)}
.band-text{left:133px;top:490px;width:480px;font-size:7.5px;line-height:14px;color:var(--text)}
.team{left:626px;top:473px;width:167px;height:37px;font-size:12px}

/* services */
.section-title{font-size:15px;font-weight:400;color:var(--brand)}
.card{top:588px;width:154px}
.card .pic{width:154px;height:109px}
.card h3{margin-top:9px;font-size:8.5px;font-weight:400;color:var(--brand)}
.card p{margin-top:5px;font-size:6.5px;line-height:13.4px;color:var(--muted)}
.rule{left:0;top:786px;width:926px;height:1px;background:var(--rule)}

/* testimonial */
.quote-title{left:0;top:815px;width:926px;text-align:center;font-size:17px}
.quote{left:229px;top:862px;width:462px;font-size:7.5px;line-height:15.5px;font-style:italic;color:var(--text)}
.quote-thanks{left:229px;top:915px;font-size:7.5px;font-style:italic;color:var(--brand)}
.qmark{font-family:Georgia,serif;font-size:26px;color:#c8c8c8}

/* referee */
.referee{left:133px;top:973px;width:661px;height:65px;background:#f1f1f1;border:1px solid #e2e2e2}
.referee-text{left:158px;top:999px;font-size:12px;color:#666}
.contact-btn{left:622px;top:988px;width:160px;height:37px;font-size:12px}

/* clients */
.client{top:1063px;width:115px;height:55px;border:1px solid #cfcfcf;display:flex;align-items:center;justify-content:center;font-size:11px;font-weight:500;color:var(--brand);gap:5px}
.client i{width:9px;height:9px;background:var(--brand);display:block}

/* footer */
.footer{left:0;top:1141px;width:926px;height:59px;background:var(--footer)}
.footer-nav{left:134px;top:1165px;font-size:7px;color:#cfcfcf;word-spacing:1px}
.footer-nav span{margin:0 9px;color:#999}
.copy{left:643px;top:1165px;font-size:7px;color:#cfcfcf}
</style>
</head>
<body>
<!-- header -->
<div class="abs logo">quorvane<span class="logo-dot"></span></div>
<div class="abs logo-sub">HEALTHCARE EDUCATION</div>
<div class="abs social"><span></span><span></span><span></span><span></span><span></span><span></span></div>
<div class="abs btn login">Client Login</div>

<nav class="abs nav">
  <a class="active">Home</a>
  <a style="left:248px">Who we are</a>
  <a style="left:349px">What we do</a>
  <a style="left:449px">Some of our work</a>
  <a style="left:573px">Who we work with</a>
  <a style="left:699px">Contact us</a>
</nav>

<!-- hero -->
<div class="abs hero"></div>
<div class="abs hero-art" role="img" aria-label="Glowing blue illustration of a human head in profile with the brain visible"></div>
<div class="abs hero-title">Quorvane</div>
<div class="abs hero-sub">Healthcare Education</div>
<div class="abs hero-lead">At Quorvane we are healthcare communication specialists;<br>this means we're scientists, journalists and marketers rolled into one.</div>
<div class="abs hero-small">As you can see we provide all the things you'd expect from a top-class healthcare communications agency, but we have the depth of technical understanding and creative flair to produce sophisticated and memorable materials and programs, including</div>
<svg class="abs arrow" style="left:34px;top:254px" viewBox="0 0 40 40"><circle cx="20" cy="20" r="18" fill="none" stroke="rgba(255,255,255,.25)" stroke-width="2"/><path d="M24 12 14 20l10 8z" fill="rgba(255,255,255,.25)"/></svg>
<svg class="abs arrow" style="left:848px;top:254px" viewBox="0 0 40 40"><circle cx="20" cy="20" r="18" fill="none" stroke="rgba(255,255,255,.25)" stroke-width="2"/><path d="M16 12l10 8-10 8z" fill="rgba(255,255,255,.25)"/></svg>

<!-- pre-launch band -->
<div class="abs band"></div>
<h2 class="abs band-title">Looking for something different pre-launch?</h2>
<p class="abs band-text">Quorvane have developed a unique tool for the online management of drug delivery, ideal for implementation in early access and special needs programs.</p>
<div class="abs btn team">Meet the quorvane team</div>

<!-- what we do -->
<h2 class="abs section-title" style="left:133px;top:551px">What we do</h2>
<svg class="abs" style="left:764px;top:556px" width="30" height="12" viewBox="0 0 30 12"><path d="M8 1 3 6l5 5M22 1l5 5-5 5" fill="none" stroke="#ccc" stroke-width="1.2"/></svg>

<div class="abs card" style="left:133px"><div class="pic" role="img" aria-label="Hands holding a small globe" style="background:linear-gradient(#f4f4f4,#e4d4c8)"></div><h3>PROMOTION</h3><p>Quorvane can help you promote your brand – from the development of strategic communication campaigns to the creation...</p></div>
<div class="abs card" style="left:302px"><div class="pic" role="img" aria-label="Scientists working in a laboratory" style="background:linear-gradient(135deg,#dfe6ec,#9fb8cc)"></div><h3>EDUCATION</h3><p>Quorvane can help you promote your brand – from the development of strategic communication campaigns to the creation...</p></div>
<div class="abs card" style="left:471px"><div class="pic" role="img" aria-label="Blue x-ray figure running beside a heartbeat line" style="background:linear-gradient(135deg,#3f8fde,#1a5fb0)"></div><h3>PROGRAMS</h3><p>Quorvane can help you promote your brand – from the development of strategic communication campaigns to the creation...</p></div>
<div class="abs card" style="left:640px"><div class="pic" role="img" aria-label="Team of medical professionals in an office" style="background:linear-gradient(135deg,#e8e8e8,#c9c6c8)"></div><h3>MEETINGS</h3><p>Quorvane can help you promote your brand – from the development of strategic communication campaigns to the creation...</p></div>

<div class="abs rule"></div>

<!-- testimonial -->
<h2 class="abs section-title quote-title">What clients say</h2>
<div class="abs qmark" style="left:189px;top:848px">&ldquo;</div>
<div class="abs qmark" style="left:718px;top:882px">&rdquo;</div>
<p class="abs quote">Congratulations &amp; many thanks for your seriously wonderful &amp; successful work on the weekend. I'm especially grateful for the calm,<br>cool &amp; very clever work done in managing all the planning process before I even came on board – truly outstanding</p>
<p class="abs quote-thanks">Thank you for all your help with making the meeting the huge success that it was</p>
<svg class="abs" style="left:126px;top:870px" width="12" height="22" viewBox="0 0 12 22"><path d="M10 1 2 11l8 10" fill="none" stroke="#ccc" stroke-width="1.5"/></svg>
<svg class="abs" style="left:786px;top:870px" width="12" height="22" viewBox="0 0 12 22"><path d="M2 1l8 10-8 10" fill="none" stroke="#ccc" stroke-width="1.5"/></svg>

<!-- referee -->
<div class="abs referee"></div>
<p class="abs referee-text">Want to speak to a referee directly? Call us and we will make the arrangements.</p>
<div class="abs btn contact-btn">Contact Us Today</div>

<!-- clients -->
<svg class="abs" style="left:121px;top:1085px" width="6" height="10" viewBox="0 0 6 10"><path d="M5 1 1 5l4 4" fill="none" stroke="#ccc"/></svg>
<div class="abs client" style="left:143px">Meridane<i></i></div>
<div class="abs client" style="left:275px">Holtberg Pharma</div>
<div class="abs client" style="left:407px">Alcyra</div>
<div class="abs client" style="left:539px">Tellivo</div>
<div class="abs client" style="left:671px"><i></i>Norvessa</div>
<svg class="abs" style="left:800px;top:1085px" width="6" height="10" viewBox="0 0 6 10"><path d="M1 1l4 4-4 4" fill="none" stroke="#ccc"/></svg>

<!-- footer -->
<footer class="abs footer"></footer>
<div class="abs footer-nav">Home<span>|</span>Who we are<span>|</span>What we do<span>|</span>Some of our work<span>|</span>Who we work with<span>|</span>Contact us</div>
<div class="abs copy">Copyrights © 2013. Quorvane. All rights Reserved.</div>
</body>
</html>
```